Educational Construction Organization needs Flyer for Upcoming Forum

We need a SAVE THE DATE Flyer for our 2020 Ravteq Forum. We work with Architects, Engineers, Contractors and Owners in the design and construction industry. Our mission is to evolve the capital projects industry through sharing of knowledge for optimized leadership, delivery and performance. The final design should communicate the connection between these industry professionals, our mission, and the Forum theme and byline.
Updates

Need extra days to review

Target Market(s)

Design and construction industry.

Industry/Entity Type

Construction

Font styles to use
Sans Serif

Colors

Designer to choose colors to be used in the design.

Requirements
Must have
• Title, By-line, 3 key topics, Date and location. Design that implements the theme with graphic(s) (not just text).
• NEW TITLE: FUTURE PROOFING: Connecting the dots to make sense of the "SMART" City
• 3 Key Topics: Smart Cities, Smart Institutions, Smart Connections
• Date: April 1-3, 2020
• Location: San Antonio, TX
Nice to have
• Please review attached problem statement for a better understanding of what this Forum will focus on when designing your graphic for the flyer.

```html
<!DOCTYPE html>
<html lang="en">
<head>
<meta charset="utf-8">
<title>Making Sense of the Smart City – 2020 Ravteq Forum</title>
<link rel="stylesheet" href="https://fonts.googleapis.com/css2?family=Archivo:wght@800;900&family=Asap+Condensed:ital,wght@0,500;0,600;1,500&family=Poppins:wght@400&display=swap">
<style>
  :root {
    --blue: #1f4496;
    --green: #8dbb3e;
    --green-light: #9ccb45;
    --grey: #55565a;
    --text-grey: #4a4a4c;
    --sky: #eef3f7;
    --water: #5fc8ee;
    --white: #ffffff;
  }
  * { margin: 0; padding: 0; box-sizing: border-box; }
  html, body { width: 900px; height: 1200px; overflow: hidden; background: var(--white); }
  .flyer {
    position: relative;
    width: 900px;
    height: 1200px;
    background: var(--white);
    font-family: "Asap Condensed", "Arial Narrow", sans-serif;
  }
  .brand {
    position: absolute;
    left: 228px;
    top: 46px;
    display: flex;
    align-items: center;
    gap: 28px;
  }
  .brand-mark {
    width: 132px;
    height: 132px;
    border-radius: 50%;
    background: var(--blue);
  }
  .brand-text { display: flex; flex-direction: column; }
  .brand-name {
    font-family: "Poppins", sans-serif;
    font-weight: 400;
    font-size: 72px;
    line-height: 1;
    color: var(--grey);
    letter-spacing: 1px;
    border-bottom: 2px solid var(--grey);
    padding-bottom: 4px;
  }
  .brand-tagline {
    margin-top: 8px;
    font-size: 17px;
    font-weight: 500;
    color: var(--green);
  }
  .header-swoosh { position: absolute; left: 0; top: 190px; width: 900px; height: 110px; }
  .title {
    position: absolute;
    top: 298px;
    width: 100%;
    text-align: center;
    font-family: "Archivo", sans-serif;
    font-weight: 900;
    font-size: 58px;
    line-height: 58px;
    color: var(--blue);
    letter-spacing: 0.5px;
  }
  .byline {
    position: absolute;
    top: 420px;
    width: 100%;
    text-align: center;
    font-style: italic;
    font-weight: 500;
    font-size: 25px;
    line-height: 30px;
    color: var(--text-grey);
  }
  .city-scene {
    position: absolute;
    left: 0;
    top: 488px;
    width: 900px;
    height: 336px;
    background:
      linear-gradient(to bottom, transparent 0 86%, var(--green) 86% 89%, var(--water) 89% 100%),
      linear-gradient(to bottom, var(--white) 0%, var(--sky) 35%, #c9d3dd 70%, #8fa0b4 86%);
  }
  .topics-banner { position: absolute; left: 224px; top: 820px; width: 460px; height: 78px; }
  .topics-banner svg { position: absolute; inset: 0; }
  .topics-banner h2 {
    position: relative;
    text-align: center;
    font-weight: 600;
    font-size: 50px;
    line-height: 78px;
    color: var(--blue);
    letter-spacing: -1px;
  }
  .topic {
    position: absolute;
    top: 928px;
    height: 112px;
    display: flex;
    align-items: center;
  }
  .topic-number {
    font-family: "Archivo", sans-serif;
    font-weight: 900;
    font-size: 118px;
    line-height: 100px;
    color: var(--blue);
  }
  .topic-label {
    position: relative;
    margin-left: 10px;
    font-weight: 500;
    font-size: 22px;
    line-height: 25px;
    color: var(--blue);
    white-space: nowrap;
  }
  .topic-arc {
    position: absolute;
    left: -16px;
    top: 50%;
    width: 114px;
    height: 114px;
    margin-top: -57px;
    overflow: visible;
  }
  .event-bar { position: absolute; left: 75px; top: 1069px; width: 760px; height: 80px; }
  .event-bar svg { position: absolute; inset: 0; }
  .event-date, .event-place {
    position: absolute;
    top: 0;
    line-height: 80px;
    font-weight: 600;
    font-size: 46px;
  }
  .event-date { left: 44px; color: var(--green-light); }
  .event-place { left: 380px; color: var(--blue); }
</style>
</head>
<body>
<main class="flyer">
  <header class="brand">
    <div class="brand-mark"></div>
    <div class="brand-text">
      <span class="brand-name">Ravteq</span>
      <span class="brand-tagline">Ravteq Institute for Project Leadership</span>
    </div>
  </header>

  <svg class="header-swoosh" viewBox="0 0 900 110" aria-hidden="true">
    <path d="M0 98 Q450 -40 900 98 L900 90 Q450 -62 0 90 Z" fill="var(--grey)"/>
    <path d="M0 110 Q450 -22 900 110 L900 96 Q450 -40 0 96 Z" fill="var(--green)"/>
  </svg>

  <h1 class="title">MAKING SENSE<br>OF THE SMART CITY</h1>
  <p class="byline">By-Line: Connecting the Dots for Dynamic Planning,<br>Design and Delivery</p>

  <div class="city-scene" role="img" aria-label="Illustration of a smart city skyline with wind turbines, solar panels, an elevated train and green rooftops beside a river"></div>

  <div class="topics-banner">
    <svg viewBox="0 0 460 78" preserveAspectRatio="none" aria-hidden="true">
      <polygon points="0,0 460,0 432,78 28,78" fill="var(--green)"/>
    </svg>
    <h2>3 KEY TOPICS</h2>
  </div>

  <div class="topic" style="left:129px">
    <span class="topic-number">1</span>
    <span class="topic-label">
      <svg class="topic-arc" viewBox="0 0 114 114" aria-hidden="true">
        <path d="M22 10 A56 56 0 1 1 22 104" fill="none" stroke="var(--blue)" stroke-width="1.6"/>
      </svg>
      SMART<br>CITIES
    </span>
  </div>

  <div class="topic" style="left:313px">
    <span class="topic-number">2</span>
    <span class="topic-label">
      <svg class="topic-arc" viewBox="0 0 114 114" aria-hidden="true">
        <path d="M22 10 A56 56 0 0 1 112 46 M112 70 A56 56 0 0 1 22 104" fill="none" stroke="var(--blue)" stroke-width="1.6"/>
      </svg>
      SMART<br>INSTITUTIONS
    </span>
  </div>

  <div class="topic" style="left:545px">
    <span class="topic-number">3</span>
    <span class="topic-label">
      <svg class="topic-arc" viewBox="0 0 114 114" aria-hidden="true">
        <path d="M22 10 A56 56 0 0 1 112 46 M112 70 A56 56 0 0 1 22 104" fill="none" stroke="var(--blue)" stroke-width="1.6"/>
      </svg>
      SMART<br>CONNECTIONS
    </span>
  </div>

  <div class="event-bar">
    <svg viewBox="0 0 760 80" aria-hidden="true">
      <polygon points="0,0 356,0 340,80 0,80" fill="var(--blue)"/>
      <polygon points="362,0 760,0 760,80 346,80" fill="var(--green)"/>
    </svg>
    <span class="event-date">April 1-3, 2020</span>
    <span class="event-place">@ San Antonio, TX</span>
  </div>
</main>
</body>
</html>
```